Banner Designs for Drone Defense Ad Campaign

Harbrook is a security consulting and services company that offers a service called SkyLedger. SkyLedger helps our customers identify security risks from drones and develops comprehensive protection programs. We are looking for a designer to create a banner ad in three sizes for our campaign.
Target Market(s)
Our campaign is geared to the sports and entertainment industry, specifically large event venues and their security operation.
Industry/Entity Type
Security
Font styles to use
Other font styles liked:
- Raleway
Requirements
Must have
- Banner Objective
The visual and textual content of the banner should prompt the viewer to quickly identify the service offered and the information that is available to download.
Banner Design
Logo: SkyLedger logo
Call to Action Button in Red: Get It Here (On Right or or Upper Right)
Title in Larger Font: Guide to UAS Risk Mitigation
Subtitle in smaller Font: 5 Steps to Develop Your Comprehensive UAS Defense Program
Background: Stadium with a drone flying in foreground
Font: Raleway
Banner Sizes
1 - 1200x670 pixels
2 - 1510x196 pixels
3 - 1200x628 pixels

```html
<!DOCTYPE html>
<html lang="en">
<head>
<meta charset="utf-8">
<title>SkyLedger Banner Set</title>
<link href="https://fonts.googleapis.com/css2?family=Montserrat:wght@700;800&family=Raleway:wght@400;500;600&family=Roboto:wght@700&display=swap" rel="stylesheet">
<style>
  :root {
    --page: #ffffff;
    --label: #1e1e1e;
    --red: #f04b4b;
    --white: #ffffff;
    --navy: #0c2430;
    --dark-photo-a: #2a2c2c;
    --dark-photo-b: #3d4238;
    --dark-photo-c: #1d211f;
    --light-photo-a: #dfe4e6;
    --light-photo-b: #f3ecd9;
    --light-photo-c: #b9b9a8;
    --stadium-green: #4f7a3a;
    --stadium-blue: #3a4a78;
    --drone-white: #e8e8e4;
    --drone-dark: #2b2f33;
  }
  * { margin: 0; padding: 0; box-sizing: border-box; }
  html, body { width: 696px; height: 1200px; overflow: hidden; background: var(--page); }
  body { position: relative; font-family: "Raleway", sans-serif; }

  .size-label {
    position: absolute; left: 0; width: 696px; text-align: center;
    font-family: "Roboto", sans-serif; font-weight: 700; font-size: 29px;
    color: var(--label); letter-spacing: 0.5px; line-height: 1;
  }

  .banner { position: absolute; overflow: hidden; box-shadow: 0 8px 24px rgba(0,0,0,0.28); }
  .banner-photo { position: absolute; inset: 0; }
  .scene-area, .drone-area { position: absolute; }

  .brand { position: absolute; line-height: 1; }
  .brand-name { display: block; font-family: "Raleway", sans-serif; font-weight: 500; }
  .brand-by { display: block; text-align: right; font-family: "Raleway", sans-serif; font-weight: 400; margin-top: 1px; }

  .btn {
    position: absolute; display: flex; align-items: center; justify-content: center;
    border-radius: 999px; font-family: "Raleway", sans-serif; font-weight: 600;
  }
  .btn-solid { background: var(--red); color: var(--white); }
  .btn-outline { border: 1px solid var(--red); }

  .title { position: absolute; font-family: "Montserrat", sans-serif; font-weight: 800; line-height: 1.08; white-space: nowrap; }
  .subtitle { position: absolute; font-family: "Raleway", sans-serif; font-weight: 500; white-space: nowrap; }

  /* 1200x628 */
  .banner-feed { left: 106px; top: 162px; width: 482px; height: 252px; color: var(--white); }
  .banner-feed .banner-photo { background: linear-gradient(160deg, #3a3c38 0%, var(--dark-photo-a) 45%, var(--dark-photo-c) 100%); }
  .banner-feed .scene-area {
    left: 180px; top: 40px; width: 320px; height: 190px;
    background: radial-gradient(ellipse at 60% 55%, var(--stadium-green) 0%, rgba(79,122,58,0.55) 22%, rgba(58,74,120,0.55) 40%, rgba(90,90,85,0.35) 62%, rgba(40,42,40,0) 80%);
  }
  .banner-feed .drone-area {
    left: 290px; top: 78px; width: 185px; height: 100px;
    background: radial-gradient(ellipse at 50% 50%, var(--drone-white) 0%, rgba(232,232,228,0.75) 35%, rgba(232,232,228,0) 72%);
  }
  .banner-feed .brand { left: 30px; top: 19px; }
  .banner-feed .brand-name { font-size: 13px; }
  .banner-feed .brand-by { font-size: 6.5px; }
  .banner-feed .btn { top: 13px; width: 65px; height: 14px; font-size: 5.5px; }
  .banner-feed .btn-solid { left: 302px; }
  .banner-feed .btn-outline { left: 378px; color: var(--white); }
  .banner-feed .title { left: 30px; top: 76px; font-size: 28.5px; }
  .banner-feed .subtitle { left: 30px; top: 145px; font-size: 10.5px; line-height: 16px; }

  /* 1200x670 */
  .banner-wide { left: 106px; top: 578px; width: 482px; height: 269px; color: var(--navy); }
  .banner-wide .banner-photo { background: linear-gradient(180deg, var(--light-photo-a) 0%, var(--light-photo-b) 55%, var(--light-photo-c) 100%); }
  .banner-wide .scene-area {
    left: 0; top: 180px; width: 482px; height: 89px;
    background: linear-gradient(180deg, rgba(170,180,175,0) 0%, rgba(150,160,150,0.7) 45%, #7f8a78 100%);
  }
  .banner-wide .sun-area {
    position: absolute; left: 300px; top: 60px; width: 182px; height: 160px;
    background: radial-gradient(ellipse at 55% 60%, rgba(255,246,215,0.95) 0%, rgba(250,238,205,0.5) 45%, rgba(250,238,205,0) 75%);
  }
  .banner-wide .drone-area {
    left: 271px; top: 104px; width: 161px; height: 48px;
    background: radial-gradient(ellipse at 50% 50%, var(--drone-dark) 0%, rgba(43,47,51,0.7) 30%, rgba(43,47,51,0) 70%);
  }
  .banner-wide .brand { left: 30px; top: 19px; }
  .banner-wide .brand-name { font-size: 13px; }
  .banner-wide .brand-by { font-size: 6.5px; }
  .banner-wide .btn { top: 16px; width: 87px; height: 20px; font-size: 7.5px; }
  .banner-wide .btn-solid { left: 262px; }
  .banner-wide .btn-outline { left: 364px; color: var(--navy); background: rgba(255,255,255,0.6); }
  .banner-wide .title { left: 30px; top: 94px; font-size: 28.5px; }
  .banner-wide .subtitle { left: 30px; top: 164px; font-size: 10.5px; line-height: 16px; }

  /* 1510x196 */
  .banner-strip { left: 44px; top: 1010px; width: 607px; height: 78px; color: var(--white); }
  .banner-strip .banner-photo { background: linear-gradient(90deg, var(--dark-photo-c) 0%, var(--dark-photo-a) 45%, #3a3d38 80%, #4a4d48 100%); }
  .banner-strip .drone-area {
    left: 490px; top: 5px; width: 83px; height: 62px;
    background: radial-gradient(ellipse at 50% 50%, var(--drone-white) 0%, rgba(232,232,228,0.75) 35%, rgba(232,232,228,0) 72%);
  }
  .banner-strip .brand { left: 34px; top: 22px; }
  .banner-strip .brand-name { font-size: 16px; }
  .banner-strip .brand-by { font-size: 8px; }
  .banner-strip .title { left: 178px; top: 9px; font-size: 16.5px; line-height: 1.15; }
  .banner-strip .subtitle { left: 178px; top: 52px; font-size: 6px; line-height: 9px; font-weight: 600; }
  .banner-strip .btn { left: 356px; width: 87px; height: 19px; font-size: 7.5px; }
  .banner-strip .btn-solid { top: 16px; }
  .banner-strip .btn-outline { top: 42px; color: var(--white); }
</style>
</head>
<body>

  <div class="size-label" style="top:91px">1200x628</div>
  <section class="banner banner-feed">
    <div class="banner-photo" role="img" aria-label="Darkened aerial photo of a city district around a large football stadium"></div>
    <div class="scene-area" role="img" aria-label="Stadium bowl with blue seating and green pitch"></div>
    <div class="drone-area" role="img" aria-label="White quadcopter drone hovering in the foreground"></div>
    <div class="brand"><span class="brand-name">SkyLedger</span><span class="brand-by">By Harbrook</span></div>
    <a class="btn btn-solid">Call to Action</a>
    <a class="btn btn-outline">Get It Here</a>
    <h1 class="title">Guide to UAS<br>Risk Mitigation</h1>
    <p class="subtitle">5 Steps to Develop Your Comprehensive UAS<br>Defense Program</p>
  </section>

  <div class="size-label" style="top:507px">1200x670</div>
  <section class="banner banner-wide">
    <div class="banner-photo" role="img" aria-label="Hazy sunlit sky over a coastal city"></div>
    <div class="sun-area" role="img" aria-label="Low sun glowing over the sea"></div>
    <div class="scene-area" role="img" aria-label="Domed stadium and bridges along the waterfront"></div>
    <div class="drone-area" role="img" aria-label="Dark folding drone flying in the foreground"></div>
    <div class="brand"><span class="brand-name">SkyLedger</span><span class="brand-by">By Harbrook</span></div>
    <a class="btn btn-solid">Call to Action</a>
    <a class="btn btn-outline">Get It Here</a>
    <h1 class="title">Guide to UAS<br>Risk Mitigation</h1>
    <p class="subtitle">5 Steps to Develop Your Comprehensive UAS<br>Defense Program</p>
  </section>

  <div class="size-label" style="top:939px">1510x196</div>
  <section class="banner banner-strip">
    <div class="banner-photo" role="img" aria-label="Darkened aerial view of a stadium district"></div>
    <div class="drone-area" role="img" aria-label="White quadcopter drone at the right"></div>
    <div class="brand"><span class="brand-name">SkyLedger</span><span class="brand-by">By Harbrook</span></div>
    <h1 class="title">Guide to UAS<br>Risk Mitigation</h1>
    <p class="subtitle">5 Steps to Develop Your Comprehensive UAS<br>Defense Program</p>
    <a class="btn btn-solid">Call to Action</a>
    <a class="btn btn-outline">Get It Here</a>
  </section>

</body>
</html>
```